Visitenkarten-Design
Zielgruppe
Malerbetrieb
Zielgruppe: Private Haushalte, Hausverwaltungen
Aufgabenstellung
Logo ist vorhanden
Lorenz Dallmer
Malermeister

```html
<!DOCTYPE html>
<html lang="de">
<head>
<meta charset="utf-8">
<title>Visitenkarte Malereibetrieb Dallmer</title>
<link rel="stylesheet" href="https://fonts.googleapis.com/css2?family=Raleway:wght@400;500;700&family=Open+Sans:wght@400;600&display=swap">
<style>
  :root {
    --stage: #000000;
    --paper: #ffffff;
    --ink: #26292d;
    --muted: #8a8a8a;
    --cyan: #2aa0dc;
    --deep-blue: #0a6fb8;
    --yellow: #f6e51c;
    --magenta: #c2188b;
    --tab: #3a3a3a;
  }
  * { margin: 0; padding: 0; box-sizing: border-box; }
  html, body { width: 1200px; height: 1200px; overflow: hidden; background: var(--stage); }
  .canvas { position: relative; width: 1200px; height: 1200px; background: var(--stage); }

  .card { position: absolute; overflow: hidden; }

  /* Front */
  .card-front { left: 361px; top: 86px; width: 575px; height: 373px; background: var(--paper); }
  .brand { position: absolute; right: 37px; text-align: right; color: var(--ink);
           font-family: "Raleway", sans-serif; line-height: 1; }
  .card-front .brand { top: 28px; }
  .brand-name { display: block; font-weight: 700; font-size: 48px; letter-spacing: 1px; }
  .brand-trade { display: block; font-weight: 500; font-size: 27px; letter-spacing: 0.3px; margin-top: 6px; }
  .tagline { position: absolute; font-family: "Open Sans", sans-serif; font-weight: 600; }
  .card-front .tagline { right: 37px; top: 120px; font-size: 13px; color: var(--muted); }

  .holder { position: absolute; left: 40px; top: 220px; color: var(--ink); }
  .holder-name { font-family: "Raleway", sans-serif; font-weight: 500; font-size: 25px; letter-spacing: 0.5px; }
  .holder-role { font-family: "Raleway", sans-serif; font-weight: 500; font-size: 15px; letter-spacing: 1.5px; margin-top: 4px; }

  .contacts { position: absolute; left: 311px; top: 186px; list-style: none;
              font-family: "Raleway", sans-serif; font-size: 16px; color: var(--ink); }
  .contacts li { display: flex; align-items: flex-start; gap: 7px; line-height: 25px; margin-bottom: 2px; }
  .contacts svg { width: 12px; height: 12px; margin-top: 6px; flex: none; }

  .front-stripe { position: absolute; left: 0; top: 337px; width: 575px; height: 36px; }
  .web { position: absolute; right: 12px; top: 342px; display: flex; align-items: center; gap: 6px;
         font-family: "Raleway", sans-serif; font-weight: 500; font-size: 16px; color: var(--paper); }
  .web svg { width: 13px; height: 13px; }

  /* Back */
  .card-back { left: 358px; top: 566px; width: 580px; height: 376px; background: var(--cyan); }
  .band { position: absolute; left: 0; width: 100%; height: 18px; }
  .band-top { top: 34px; background: linear-gradient(90deg, var(--magenta) 0%, var(--magenta) 20%, #d77fa6 34%, var(--yellow) 52%, #7fbfc9 72%, var(--deep-blue) 82%, var(--deep-blue) 100%); }
  .band-bottom { top: 322px; background: linear-gradient(90deg, var(--deep-blue) 0%, var(--deep-blue) 18%, #7fbfc9 32%, var(--yellow) 50%, #d77fa6 68%, var(--magenta) 80%, var(--magenta) 100%); }
  .card-back .brand { left: 0; right: 0; top: 112px; text-align: center; }
  .card-back .brand-name { font-size: 70px; letter-spacing: 2px; }
  .card-back .brand-trade { font-size: 35px; margin-top: 8px; }
  .card-back .tagline { left: 0; right: 0; top: 233px; text-align: center; font-size: 17px; color: var(--paper); }
</style>
</head>
<body>
<div class="canvas">

  <section class="card card-front" aria-label="Visitenkarte Vorderseite">
    <div class="brand">
      <span class="brand-name">DALLMER</span>
      <span class="brand-trade">MALEREIBETRIEB</span>
    </div>
    <p class="tagline">Sorgfalt in jeder Schicht Farbe</p>

    <div class="holder">
      <p class="holder-name">LORENZ DALLMER</p>
      <p class="holder-role">Malermeister</p>
    </div>

    <ul class="contacts">
      <li>
        <svg viewBox="0 0 12 12"><path d="M6 1a3.5 3.5 0 0 0-3.5 3.5C2.5 7.5 6 11 6 11s3.5-3.5 3.5-6.5A3.5 3.5 0 0 0 6 1z" fill="none" stroke="var(--cyan)" stroke-width="1.2"/><circle cx="6" cy="4.5" r="1.2" fill="var(--cyan)"/></svg>
        <span>Lindenkamp 47 b<br>22391 Nordstadt</span>
      </li>
      <li>
        <svg viewBox="0 0 12 12"><path d="M3 1l2 2.5-1.2 1.3a7 7 0 0 0 3.4 3.4L8.5 7 11 9l-1.3 1.8C5.5 10.5 1.5 6.5 1.2 2.3z" fill="var(--cyan)"/></svg>
        <span>0176- 4 318 209</span>
      </li>
      <li>
        <svg viewBox="0 0 12 12"><rect x="1" y="3" width="10" height="7" fill="var(--cyan)"/><path d="M1 3l5 4 5-4" fill="none" stroke="var(--paper)" stroke-width="1"/></svg>
        <span>info@malereibetrieb-dallmer.de</span>
      </li>
    </ul>

    <svg class="front-stripe" viewBox="0 0 575 36" preserveAspectRatio="none" aria-hidden="true">
      <defs>
        <linearGradient id="frontGrad" x1="0" x2="1" y1="0" y2="0">
          <stop offset="0" stop-color="#2aa0dc"/>
          <stop offset="0.22" stop-color="#2aa0dc"/>
          <stop offset="0.5" stop-color="#f6e51c"/>
          <stop offset="0.68" stop-color="#e0a0a0"/>
          <stop offset="0.82" stop-color="#c2188b"/>
          <stop offset="1" stop-color="#c2188b"/>
        </linearGradient>
      </defs>
      <path d="M0 10 H262 L252 23 H0 Z" fill="url(#frontGrad)"/>
      <path d="M575 0 V36 H250 C270 33 276 18 288 8 C294 2 300 0 312 0 Z" fill="var(--tab)"/>
    </svg>
    <div class="web">
      <svg viewBox="0 0 14 14"><circle cx="7" cy="7" r="5.8" fill="none" stroke="#fff" stroke-width="1.2"/><ellipse cx="7" cy="7" rx="2.4" ry="5.8" fill="none" stroke="#fff" stroke-width="1"/><path d="M1.2 7h11.6" stroke="#fff" stroke-width="1"/></svg>
      <span>www.malereibetrieb-dallmer.de</span>
    </div>
  </section>

  <section class="card card-back" aria-label="Visitenkarte Rückseite">
    <div class="band band-top"></div>
    <div class="brand">
      <span class="brand-name">DALLMER</span>
      <span class="brand-trade">MALEREIBETRIEB</span>
    </div>
    <p class="tagline">Sorgfalt in jeder Schicht Farbe</p>
    <div class="band band-bottom"></div>
  </section>

</div>
</body>
</html>
```